K5Lesson WebSite

an educational website about tutoring, client will be surfing this site looking for a tutor, please see the attached images because the contains exactly what we need.
Updates

Project Deadline Extended Reason: something went wrong with the uploaded files, we are very sorry.thank you PixelBazaar for the 5 days extension.now there is a 3 images describing the content of the three pages.good luck Added Friday, August 5, 2016

Target Market(s)

everyone

Industry/Entity Type

Education

Number of Pages Required

3 page

Font styles to use
Other font styles liked:
• something looks good in Arabic and english like "Droid Arabic Kufi"

Requirements
Must have
• the logo we attached, responsive design, simple, also try as much as you can Centering texts and layout because this website will have an Arabic version, Arabic is a Right-to-Left Language.
• a change language button,
Nice to have
• educational gestures.
• Centered texts and layout because this website will have an Arabic version, Arabic is a Right-to-Left Language.
• we have a web designer and we can download any template and add our logo and text to it, but.....
• we need creativity, so please stick to the contents in the images we attached, we need something very simple, more like a varnel home page with little touch of filtering fields like the 5 dropdownlist and the gender selection buttons.
• try not to go far away from the contents we specified in the images, use less images or dont use images at all, try not to make the client scroll down,
Should not have
• too much colors or noisy layout or heavy media

```html
<!DOCTYPE html>
<html lang="en">
<head>
<meta charset="utf-8">
<title>K5Lesson – Personalized Tutoring</title>
<link rel="stylesheet" href="https://fonts.googleapis.com/css2?family=Lato:wght@300;400;700;900&display=swap">
<style>
:root{
  --blue:#1c8ed6;
  --blue-dark:#1565b4;
  --footer:#1f6cbd;
  --orange:#f26a23;
  --green:#8cc63e;
  --ink:#333;
  --muted:#666;
  --pale:#e9f4fb;
  --line:#c9d6df;
}
*{box-sizing:border-box;margin:0;padding:0}
html,body{width:1200px;height:3214px;overflow:hidden}
body{font-family:'Lato',sans-serif;color:var(--ink);background:#fff;position:relative}
a{text-decoration:none;color:inherit}

/* header */
.site-header{height:80px;display:flex;align-items:center;justify-content:space-between;padding:0 80px}
.brand{display:flex;align-items:center;gap:10px;font-size:30px;font-weight:700;color:var(--blue)}
.brand-mark{width:30px;height:30px;background:var(--blue)}
.main-nav{display:flex;gap:30px;font-size:14px;color:#555}
.main-nav a.active{color:var(--blue);border-bottom:3px solid var(--blue);padding-bottom:8px}

/* hero */
.hero{position:relative;height:539px}
.hero-photo{position:absolute;inset:0;background:linear-gradient(90deg,#f7f7f5 0%,#eceae6 30%,#c9c3bb 55%,#8fa1b3 80%,#d8d6d2 100%)}
.hero-copy{position:absolute;left:80px;top:145px}
.hero-title{font-size:54px;font-weight:900;color:var(--blue-dark)}
.hero-sub{font-size:42px;font-weight:300;line-height:1.25;margin-top:10px;color:#222}
.btn{display:inline-flex;align-items:center;justify-content:center;color:#fff;font-size:19px}
.btn-hero{background:var(--orange);width:236px;height:48px;margin-top:30px}

/* intro band */
.intro-band{position:relative;height:135px;background:var(--blue);text-align:center;color:#fff;padding-top:18px}
.intro-band h2{font-size:34px;font-weight:400}
.intro-band p{color:#c7ee8a;font-size:16px;line-height:1.4;width:1000px;margin:8px auto 0}
.intro-band::after{content:"";position:absolute;left:585px;bottom:-16px;border:16px solid transparent;border-bottom:0;border-top-color:var(--blue)}

/* section titles */
.section-title{text-align:center;font-size:30px;font-weight:400;color:var(--blue)}
.title-rule{width:320px;height:2px;background:var(--line);margin:14px auto 0}

/* services */
.services{height:440px;padding-top:58px}
.service-grid{display:flex;justify-content:center;gap:0;margin-top:32px;padding:0 80px}
.service{width:267px;text-align:center}
.service-icon{width:110px;height:110px;margin:0 auto}
.service h3{font-size:18px;font-weight:400;margin-top:22px}
.service p{font-size:12px;color:var(--muted);line-height:1.5;width:220px;margin:18px auto 0}
.service .more{display:block;font-size:12px;margin-top:10px;color:var(--green)}
.service .more.alt{color:var(--orange)}

/* promo banner */
.promo{position:relative;height:446px}
.promo-photo{position:absolute;inset:0;background:linear-gradient(90deg,#fdf6f1 0%,#f6e6dc 30%,#c9a88f 45%,#9b7f74 65%,#8a7b80 85%,#b8a79c 100%)}
.promo-copy{position:absolute;left:80px;top:70px;line-height:1.15}
.promo-copy .soft{font-size:38px;font-weight:300}
.promo-copy .bold{font-size:58px;font-weight:900}
.is-blue{color:var(--blue-dark)}
.is-orange{color:var(--orange)}
.role-buttons{display:flex;gap:14px;margin-top:22px}
.role-btn{height:38px;padding:0 14px;font-size:15px;gap:8px}
.role-btn.student{background:var(--blue-dark)}
.role-btn.tutor{background:var(--orange)}
.role-btn i{width:14px;height:14px;background:#fff;border-radius:50%}

/* testimonials */
.testimonials{height:492px;padding-top:48px}
.quote{position:relative;width:1040px;margin:34px auto 0;text-align:center;font-size:14px;color:var(--muted);line-height:1.6}
.quote::before,.quote::after{position:absolute;font-size:70px;color:var(--green);font-weight:900;line-height:1}
.quote::before{content:"\201C";left:-38px;top:-8px}
.quote::after{content:"\201D";right:-38px;top:20px}
.featured-name{position:absolute;left:500px;top:1851px;width:200px;height:48px;background:var(--orange);color:#fff;text-align:center;font-size:15px;padding-top:6px}
.featured-name small{display:block;font-size:10px}
.featured-name::after{content:"";position:absolute;left:92px;bottom:-8px;border:8px solid transparent;border-bottom:0;border-top-color:var(--orange)}
.avatar{position:absolute;border-radius:50%;background:radial-gradient(circle at 50% 40%,#d6b49a,#7c8da0)}
.avatar.small{width:98px;height:98px;top:1974px}
.avatar.large{width:164px;height:164px;left:518px;top:1908px;border:6px solid var(--blue);background:radial-gradient(circle at 50% 40%,#d8b79c,#3d97d8)}

/* articles */
.reading{height:428px;background:var(--pale);display:flex;gap:68px;padding:54px 75px 0 81px}
.reading-col{width:489px}
.col-head{display:flex;justify-content:space-between;align-items:center;border-bottom:1px solid #9fb3c2;padding-bottom:10px}
.col-head h3{font-size:20px;font-weight:400}
.pager{color:var(--line);font-size:20px;letter-spacing:6px}
.post{display:flex;gap:24px;margin-top:28px}
.post-thumb{width:133px;height:133px;border:10px solid #1d3a5c;background:linear-gradient(135deg,#f4f1e6,#d9cfb4)}
.post h4{font-size:14px;font-weight:700;margin-top:2px}
.post p{font-size:11px;color:#555;line-height:1.45;margin-top:10px;width:330px}
.post .byline{font-size:11px;margin-top:8px}

/* partners */
.partners{height:329px;padding-top:56px;position:relative}
.partner-row{display:flex;gap:47px;justify-content:center;margin-top:44px}
.partner{width:171px;height:98px;border:1px solid #ccc;display:flex;align-items:center;justify-content:center}
.partner span{display:block}
.slider-arrow{position:absolute;top:162px}
.slider-arrow.prev{left:24px}
.slider-arrow.next{right:24px}

/* footer */
.site-footer{height:282px;background:var(--footer);color:#fff;display:flex;padding:48px 0 0 79px}
.foot-col h4{font-size:18px;font-weight:300;color:#cfe2f5;border-bottom:1px solid #4f8fd0;padding-bottom:10px;margin-bottom:14px}
.col-links{width:223px}.col-links h4{width:180px}
.col-contact{width:337px}.col-contact h4{width:290px}
.col-news{width:295px}.col-news h4{width:260px}
.col-follow{width:200px}.col-follow h4{width:180px}
.foot-col li{list-style:none;font-size:12px;line-height:1.6;display:flex;align-items:flex-start;gap:8px}
.col-links li::before{content:"";width:4px;height:4px;border-radius:50%;background:#fff;margin-top:8px}
.col-contact li{margin-bottom:12px;font-weight:700}
.col-contact svg{flex:none;margin-top:3px}
.col-news p{font-size:12px;line-height:1.5;width:230px}
.email-field{width:200px;height:26px;background:#fff;color:#777;font-size:11px;padding:6px 8px;margin-top:12px}
.subscribe{display:inline-block;background:var(--orange);font-size:10px;padding:6px 10px;margin-top:14px}
.col-follow li{margin-bottom:14px;align-items:center}
.social-box{width:20px;height:20px;background:#fff;border-radius:3px}
.bottom-bar{height:43px;background:var(--green);color:#fff;font-size:11px;display:flex;justify-content:space-between;align-items:center;padding:0 80px}
.bottom-bar nav{display:flex;gap:24px}
</style>
</head>
<body>

<header class="site-header">
  <a class="brand" href="#"><span class="brand-mark"></span>K5Lesson</a>
  <nav class="main-nav">
    <a class="active" href="#">Home</a><a href="#">About</a><a href="#">How It Works</a>
    <a href="#">Students &amp;Parents</a><a href="#">Tutors</a><a href="#">Blog</a><a href="#">Contact Us</a>
  </nav>
</header>

<section class="hero">
  <div class="hero-photo" role="img" aria-label="Photo of a tutor leaning over a desk helping smiling students in a bright classroom"></div>
  <div class="hero-copy">
    <h1 class="hero-title">K5 Lesson</h1>
    <p class="hero-sub">Personalized Tutoring<br>For Success.</p>
    <a class="btn btn-hero" href="#">View Our Tutors</a>
  </div>
</section>

<section class="intro-band">
  <h2>K5 Lesson Is A UK's No 1 Tutoring Services Provider.</h2>
  <p>Lorem ipsum dolor sit amet, consectetur adipiscing elit. Sed lobortis dui leo, et accumsan lacus tempor blandit. Class aptent taciti sociosqu ad litora torquent per conubia nostra, per inceptos himenaeos.</p>
</section>

<section class="services">
  <h2 class="section-title">Our Services</h2>
  <div class="title-rule"></div>
  <div class="service-grid">
    <div class="service">
      <svg class="service-icon" viewBox="0 0 110 110"><circle cx="55" cy="55" r="52" fill="none" stroke="#8cc63e" stroke-width="2.5"/><circle cx="55" cy="55" r="28" fill="none" stroke="#8cc63e" stroke-width="3"/><text x="55" y="63" text-anchor="middle" font-family="Lato,sans-serif" font-size="22" font-weight="700" fill="#8cc63e">24</text></svg>
      <h3>24/7 Access</h3>
      <p>Nullam sit amet scelerisque justo. Nullam at blandit augue, at iaculis erat. Etiam ligula cursus nec.</p>
      <a class="more" href="#">View Memebership Plans &gt;&gt;</a>
    </div>
    <div class="service">
      <svg class="service-icon" viewBox="0 0 110 110"><circle cx="55" cy="55" r="52" fill="none" stroke="#f26a23" stroke-width="2.5"/><circle cx="55" cy="50" r="24" fill="none" stroke="#f26a23" stroke-width="3"/><circle cx="55" cy="50" r="15" fill="none" stroke="#f26a23" stroke-width="2"/><text x="55" y="56" text-anchor="middle" font-family="Lato,sans-serif" font-size="16" font-weight="700" fill="#f26a23">1</text><path d="M44 72l-6 14 8-3 4 7 5-14M66 72l6 14-8-3-4 7-5-14" fill="none" stroke="#f26a23" stroke-width="2.5"/></svg>
      <h3>The Best Tutors</h3>
      <p>Nullam sit amet scelerisque justo. Nullam at blandit augue, at iaculis erat. Etiam ligula cursus nec.</p>
      <a class="more alt" href="#">See our Tutors &gt;&gt;</a>
    </div>
    <div class="service">
      <svg class="service-icon" viewBox="0 0 110 110"><circle cx="55" cy="55" r="52" fill="none" stroke="#8cc63e" stroke-width="2.5"/><circle cx="53" cy="57" r="26" fill="none" stroke="#8cc63e" stroke-width="3"/><circle cx="53" cy="57" r="16" fill="none" stroke="#8cc63e" stroke-width="3"/><circle cx="53" cy="57" r="6" fill="#8cc63e"/><path d="M53 57L78 32M72 30h8v8" fill="none" stroke="#8cc63e" stroke-width="3"/></svg>
      <h3>Personalized</h3>
      <p>Nullam sit amet scelerisque justo. Nullam at blandit augue, at iaculis erat. Etiam ligula cursus nec.</p>
      <a class="more" href="#">View Students' Testimonials &gt;&gt;</a>
    </div>
    <div class="service">
      <svg class="service-icon" viewBox="0 0 110 110"><circle cx="55" cy="55" r="52" fill="none" stroke="#f26a23" stroke-width="2.5"/><circle cx="55" cy="55" r="28" fill="none" stroke="#f26a23" stroke-width="3"/><circle cx="55" cy="55" r="6" fill="#f26a23"/><path d="M55 27v56M27 55h56M35 35l40 40M75 35L35 75" stroke="#f26a23" stroke-width="2"/></svg>
      <h3>Variety Of Subjects</h3>
      <p>Nullam sit amet scelerisque justo. Nullam at blandit augue, at iaculis erat. Etiam ligula cursus nec.</p>
      <a class="more alt" href="#">View All Subjects &gt;&gt;</a>
    </div>
  </div>
</section>

<section class="promo">
  <div class="promo-photo" role="img" aria-label="Photo of a cheerful group of students giving thumbs up around classroom desks"></div>
  <div class="promo-copy">
    <div class="soft is-blue">Make The Future</div>
    <div class="bold is-blue">Bright</div>
    <div class="soft is-orange">&amp; Lets The World</div>
    <div class="bold is-orange">Win</div>
    <div class="role-buttons">
      <a class="btn role-btn student" href="#"><i></i>I am a Student</a>
      <a class="btn role-btn tutor" href="#"><i></i>I am a Tutor</a>
    </div>
  </div>
</section>

<section class="testimonials">
  <h2 class="section-title">Students' Testimonials</h2>
  <div class="title-rule"></div>
  <p class="quote">Fusce commodo tempus nibh, ac vestibulum odio ultricies ac. Interdum et malesuada fames ac ante ipsum primis in faucibus. Integer pharetra urna in sem varius hendrerit. Nunc vel nunc a massa auctor tristique vitae ac dolor. Praesent ac venenatis ipsum, quis pellentesque leo.</p>
</section>
<div class="featured-name">Ravi Holden<small>Florida</small></div>
<div class="avatar small" style="left:82px" role="img" aria-label="Student portrait"></div>
<div class="avatar small" style="left:217px" role="img" aria-label="Student portrait"></div>
<div class="avatar small" style="left:367px" role="img" aria-label="Student portrait"></div>
<div class="avatar large" role="img" aria-label="Featured student portrait"></div>
<div class="avatar small" style="left:733px" role="img" aria-label="Student portrait"></div>
<div class="avatar small" style="left:885px" role="img" aria-label="Student portrait"></div>
<div class="avatar small" style="left:1020px" role="img" aria-label="Student portrait"></div>

<section class="reading">
  <div class="reading-col">
    <div class="col-head"><h3>Articles From Our Tutors</h3><span class="pager">&lsaquo;&rsaquo;</span></div>
    <article class="post">
      <div class="post-thumb" role="img" aria-label="Sticky note reading helpful tips"></div>
      <div><h4>Tips to Write an Awesome Thesis Statement</h4><p>Nam varius, enim ac vestibulum tincidunt, eros ligula dignissim nisl, sit amet commodo tellus quam ac libero.Nullam nec pharetra sapien, vitae laoreet est.</p><div class="byline">By: Mara Lint</div></div>
    </article>
    <article class="post">
      <div class="post-thumb" role="img" aria-label="Sticky note reading helpful tips"></div>
      <div><h4>Tips to Write an Awesome Thesis Statement</h4><p>Nam varius, enim ac vestibulum tincidunt, eros ligula dignissim nisl, sit amet commodo tellus quam ac libero.Nullam nec pharetra sapien, vitae laoreet est.</p><div class="byline">By: Mara Lint</div></div>
    </article>
  </div>
  <div class="reading-col">
    <div class="col-head"><h3>Blog</h3><span class="pager">&lsaquo;&rsaquo;</span></div>
    <article class="post">
      <div class="post-thumb" role="img" aria-label="Colourful blog lettering"></div>
      <div><h4>Tips to Write an Awesome Thesis Statement</h4><p>Nam varius, enim ac vestibulum tincidunt, eros ligula dignissim nisl, sit amet commodo tellus quam ac libero.Nullam nec pharetra sapien, vitae laoreet est.</p><div class="byline">By: Mara Lint</div></div>
    </article>
    <article class="post">
      <div class="post-thumb" role="img" aria-label="Colourful blog lettering"></div>
      <div><h4>Tips to Write an Awesome Thesis Statement</h4><p>Nam varius, enim ac vestibulum tincidunt, eros ligula dignissim nisl, sit amet commodo tellus quam ac libero.Nullam nec pharetra sapien, vitae laoreet est.</p><div class="byline">By: Mara Lint</div></div>
    </article>
  </div>
</section>

<section class="partners">
  <h2 class="section-title">Our Partners</h2>
  <div class="title-rule"></div>
  <svg class="slider-arrow prev" width="24" height="40" viewBox="0 0 24 40"><path d="M20 2L4 20l16 18" fill="none" stroke="#999" stroke-width="2"/></svg>
  <div class="partner-row">
    <div class="partner"><span style="width:110px;height:46px;background:#d8262e;border-radius:50%"></span></div>
    <div class="partner"><span style="width:54px;height:54px;background:#1457a8"></span></div>
    <div class="partner"><span style="width:120px;height:30px;background:#3a8c3d;border-radius:4px"></span></div>
    <div class="partner"><span style="width:130px;height:36px;background:#4b2a8a"></span></div>
    <div class="partner"><span style="width:64px;height:64px;background:#333;border-radius:50%"></span></div>
  </div>
  <svg class="slider-arrow next" width="24" height="40" viewBox="0 0 24 40"><path d="M4 2l16 18L4 38" fill="none" stroke="#999" stroke-width="2"/></svg>
</section>

<footer class="site-footer">
  <div class="foot-col col-links">
    <h4>Quick Links</h4>
    <ul><li>Home</li><li>About</li><li>How It Works</li><li>Students &amp;Parents</li><li>Tutors</li><li>Blog</li><li>Contact Us</li></ul>
  </div>
  <div class="foot-col col-contact">
    <h4>Contact Information</h4>
    <ul>
      <li><svg width="12" height="16" viewBox="0 0 12 16"><path d="M6 0a6 6 0 0 1 6 6c0 4-6 10-6 10S0 10 0 6a6 6 0 0 1 6-6z" fill="#fff"/><circle cx="6" cy="6" r="2" fill="#1f6cbd"/></svg>Elmweg 14, 4410 Kestrelburg,<br>Austria</li>
      <li><svg width="12" height="16" viewBox="0 0 12 16"><path d="M2 0h3l1 4-2 1c1 2 2 4 4 5l1-2 3 1v3c0 2-2 4-4 3C3 13 0 8 0 3 0 1 1 0 2 0z" fill="#fff"/></svg>+00 (01) 555 019</li>
      <li><svg width="14" height="10" viewBox="0 0 14 10"><rect width="14" height="10" fill="#fff"/><path d="M0 0l7 6 7-6" fill="none" stroke="#1f6cbd" stroke-width="1.5"/></svg>info@k5lesson.com</li>
    </ul>
  </div>
  <div class="foot-col col-news">
    <h4>Newsletter Signup</h4>
    <p>Please enter your email address below to receive our FREE newsletter</p>
    <div class="email-field">Your Email ID</div>
    <span class="subscribe">SUBSCRIBE</span>
  </div>
  <div class="foot-col col-follow">
    <h4>Follow Us</h4>
    <ul><li><span class="social-box"></span>Friendbook</li><li><span class="social-box"></span>Linkwork</li><li><span class="social-box"></span>Chirper</li><li><span class="social-box"></span>Email</li></ul>
  </div>
</footer>
<div class="bottom-bar">
  <span>Copyright@k5lesson.com, All Rights Are Reserved.</span>
  <nav><span>Join Us</span><span>Login to K5Lesson Online</span><span>Remote Presentation/Support</span></nav>
</div>

</body>
</html>
```